8 behaviours infographic

We are a portfolio of approx. 200 resources in technology within a financial services enterprise (5000-6000 employees).
Our portfolio name is Harbour and Planner Asset Services.
Our leadership team has collectively defined a set of 8 behaviours that represent how we should behave and interact amongst ourselves.
We need an infographic that can bring these behaviours to life and be displayed around the workplace on large posters where teams work (the words for the behaviours should also be incorporated into the infographic).
We have also included our team's logo, which needs to be incorporated into the infographic.
The 8 behaviours are:
- Listen & show you care
- Support Each Other
- Be Accountable
- Communicate openly
- Collaborate and leverage the collective strength of the group
- Influence the agenda
- Proactive deliberate and team focussed
- Celebrate success & have fun
Look and feel
Each slider illustrates characteristics of the customer's brand and the style your logo design should communicate.

```html
<!DOCTYPE html>
<html lang="en">
<head>
<meta charset="utf-8">
<title>Harbour and Planner Asset Services – Our 8 Behaviours</title>
<link href="https://fonts.googleapis.com/css2?family=Montserrat:wght@300;400;700;800&display=swap" rel="stylesheet">
<style>
  :root {
    --page-bg: #ffffff;
    --blue-light: #0a88c2;
    --blue-mid: #1668ab;
    --blue-deep: #1a5298;
    --blue-navy: #1d3e80;
    --ink-white: #ffffff;
    --footer-bg: #ffffff;
    --brand-blue: #1677c4;
    --icon-fill: rgba(255, 255, 255, 0.14);
  }
  * { box-sizing: border-box; margin: 0; padding: 0; }
  html, body {
    width: 1200px; height: 1200px; overflow: hidden;
    background: var(--page-bg);
    font-family: "Montserrat", sans-serif;
  }
  .poster {
    position: absolute; left: 197px; top: 30px;
    width: 806px; height: 1140px; overflow: hidden;
    box-shadow: 0 6px 24px rgba(0,0,0,0.12);
  }
  .poster-inner {
    position: absolute; left: 0; top: 0;
    width: 905px; height: 1279px;
    transform: scale(0.8906); transform-origin: 0 0;
  }
  .backdrop { position: absolute; left: 0; top: 0; width: 905px; height: 1119px; }
  .behaviour {
    position: absolute; transform: translateX(-50%);
    color: var(--ink-white); text-align: center;
    display: flex; flex-direction: column; align-items: center;
  }
  .behaviour-icon { display: block; }
  .behaviour-label {
    margin-top: 14px; font-size: 19px; line-height: 1.0;
    font-weight: 300; letter-spacing: 0.3px; white-space: nowrap;
  }
  .behaviour-label strong { font-weight: 700; }
  .celebrate-icon { position: absolute; left: 258px; top: 834px; }
  .celebrate-label {
    position: absolute; left: 570px; top: 916px;
    color: var(--ink-white); font-size: 28px; line-height: 1.05; font-weight: 300;
  }
  .celebrate-label strong { font-weight: 800; font-size: 31px; }
  .footer {
    position: absolute; left: 0; top: 1119px; width: 905px; height: 160px;
    background: var(--footer-bg);
    display: flex; align-items: center; justify-content: center;
  }
  .brand-name {
    color: var(--brand-blue); font-weight: 700; font-size: 28px; letter-spacing: 0.5px;
  }
</style>
</head>
<body>
  <main class="poster">
    <div class="poster-inner">
      <svg class="backdrop" viewBox="0 0 905 1119" aria-hidden="true">
        <rect width="905" height="1119" fill="var(--blue-deep)"/>
        <polygon points="0,0 905,0 905,40 0,495" fill="var(--blue-mid)"/>
        <polygon points="0,0 720,0 0,110" fill="var(--blue-light)"/>
        <polygon points="0,740 905,635 905,1119 0,1119" fill="var(--blue-navy)"/>
        <g class="frame-brackets" fill="none" stroke="var(--ink-white)" stroke-width="22" stroke-linecap="round" stroke-linejoin="round">
          <path d="M161,309 L161,355 Q161,389 195,389 L258,389 M161,469 L161,423 Q161,389 195,389"/>
          <path d="M742,309 L742,355 Q742,389 708,389 L645,389 M742,469 L742,423 Q742,389 708,389"/>
          <path d="M161,776 L161,820 Q161,859 200,859 L258,859"/>
          <path d="M742,776 L742,820 Q742,859 703,859 L645,859"/>
        </g>
      </svg>

      <div class="behaviour" style="left:175px; top:79px;">
        <svg class="behaviour-icon" width="120" height="100" role="img" aria-label="Line icon of an ear with sound waves"><rect width="120" height="100" rx="18" fill="var(--icon-fill)"/></svg>
        <p class="behaviour-label">Listen &amp; show<br><strong>you care</strong></p>
      </div>

      <div class="behaviour" style="left:453px; top:76px;">
        <svg class="behaviour-icon" width="120" height="104" role="img" aria-label="Line icon of hands supporting a group"><rect width="120" height="104" rx="18" fill="var(--icon-fill)"/></svg>
        <p class="behaviour-label"><strong>Support</strong><br>Each Other</p>
      </div>

      <div class="behaviour" style="left:728px; top:79px;">
        <svg class="behaviour-icon" width="110" height="100" role="img" aria-label="Line icon of a checklist clipboard with a pencil"><rect width="110" height="100" rx="18" fill="var(--icon-fill)"/></svg>
        <p class="behaviour-label">Be <strong>Accountable</strong></p>
      </div>

      <div class="behaviour" style="left:456px; top:314px;">
        <svg class="behaviour-icon" width="136" height="100" role="img" aria-label="Line icon of an open hand holding gears"><rect width="136" height="100" rx="18" fill="var(--icon-fill)"/></svg>
        <p class="behaviour-label"><strong>Collaborate</strong> and <strong>leverage</strong><br>the collective strength<br>of the group</p>
      </div>

      <div class="behaviour" style="left:183px; top:584px;">
        <svg class="behaviour-icon" width="140" height="86" role="img" aria-label="Line icon of a hand raising rising bars"><rect width="140" height="86" rx="18" fill="var(--icon-fill)"/></svg>
        <p class="behaviour-label" style="margin-top:22px;"><strong>Influence</strong> the agenda</p>
      </div>

      <div class="behaviour" style="left:448px; top:574px;">
        <svg class="behaviour-icon" width="134" height="100" role="img" aria-label="Line icon of a megaphone with sound waves"><rect width="134" height="100" rx="18" fill="var(--icon-fill)"/></svg>
        <p class="behaviour-label" style="margin-top:16px;"><strong>Communicate</strong><br>openly</p>
      </div>

      <div class="behaviour" style="left:733px; top:564px;">
        <svg class="behaviour-icon" width="144" height="112" role="img" aria-label="Line icon of three light bulbs with a tick"><rect width="144" height="112" rx="18" fill="var(--icon-fill)"/></svg>
        <p class="behaviour-label" style="margin-top:14px;"><strong>Proactive deliberate</strong><br>and team focussed</p>
      </div>

      <svg class="celebrate-icon" width="280" height="215" role="img" aria-label="Line illustration of an open hand holding a flag with fireworks"><rect width="280" height="215" rx="24" fill="var(--icon-fill)"/></svg>
      <p class="celebrate-label"><strong>Celebrate</strong><br>success &amp;<br>have fun</p>

      <footer class="footer">
        <p class="brand-name">Harbour and Planner Asset Services</p>
      </footer>
    </div>
  </main>
</body>
</html>
```